electrical contractor business card for professional modern company

I need a business card design for an electrical contractors business. I do all kinds of electricical work from new homes, air conditioning, data and communications. I have a logo design i want on it and have a good idea in my head of what i want it to look like. I like simple yet bold and professional looking. All black background is a must

Target Market(s)

Anyone needing electrical work done

Industry/Entity Type

Electrical

Contact Information for Business Card

company name- KTW Electrical and Data
person name-martin pellowe
phone number- 0418 362 927
website-ktwelec.example.com.au

Font styles to use
Sans Serif

Requirements
Must have
• email
• website
• logo
• name
• phone number
• list of work i do:
• -electrical
• -air-conditioning
• -data/communications
• -cctv/security
• -domestic/commercial/industrial
• -24hr emergency breakdown repair
Nice to have
• i would like the logo on the front side in the centre taking up most of the card with black background.
• on the rear i want the list of work i do with company info i.e. email, website, my name, phone number. rear of card also black background with orange writing to match the orange in the logo

```html
<!DOCTYPE html>
<html lang="en">
<head>
<meta charset="utf-8">
<title>KTW Electrical and Data – Business Card</title>
<link href="https://fonts.googleapis.com/css2?family=Open+Sans:wght@400;600;700&display=swap" rel="stylesheet">
<style>
  :root {
    --backdrop: #9a9a9a;
    --card: #141414;
    --card-edge: #0a0a0a;
    --ink: #f2f2f2;
    --muted: #9a9a9a;
    --orange: #e8581a;
    --orange-deep: #d9480f;
  }
  * { box-sizing: border-box; margin: 0; padding: 0; }
  html, body { width: 1200px; height: 720px; overflow: hidden; }
  body {
    background: var(--backdrop);
    font-family: "Open Sans", Arial, sans-serif;
    color: var(--ink);
    display: flex;
    align-items: center;
    justify-content: center;
    gap: 40px;
  }
  .card {
    position: relative;
    width: 560px;
    height: 320px;
    background: linear-gradient(135deg, #1c1c1c 0%, var(--card) 60%, var(--card-edge) 100%);
    box-shadow: 0 6px 18px rgba(0,0,0,0.3);
    overflow: hidden;
  }
  .brand {
    position: absolute;
    display: flex;
    align-items: center;
    gap: 10px;
    white-space: nowrap;
  }
  .brand__dot {
    width: 16px; height: 16px; border-radius: 50%;
    background: var(--orange);
    flex: none;
  }
  .brand__name {
    font-weight: 700;
    font-size: 22px;
    letter-spacing: 0.5px;
    color: var(--ink);
  }
  .website {
    position: absolute;
    top: 26px; right: 30px;
    display: flex; align-items: center; gap: 8px;
    font-size: 13px;
  }
  .website svg { width: 13px; height: 13px; }

  /* Front */
  .card--front .brand { top: 100px; left: 50%; transform: translateX(-50%); }
  .tagline {
    position: absolute;
    left: 0; right: 0; top: 232px;
    display: flex; align-items: center; gap: 16px;
  }
  .tagline__bar { height: 20px; background: var(--orange-deep); }
  .tagline__bar--left { width: 60px; }
  .tagline__bar--right { flex: 1; }
  .tagline__text {
    color: var(--orange);
    font-size: 17px;
    letter-spacing: 1.6px;
    white-space: nowrap;
  }

  /* Back */
  .card--back::after {
    content: ""; position: absolute; left: 0; right: 0; bottom: 0;
    height: 6px; background: var(--orange);
  }
  .card--back .brand { top: 96px; left: 330px; transform: translateX(-50%); }
  .person { position: absolute; top: 32px; left: 28px; }
  .person__name { color: var(--orange); font-weight: 700; font-size: 19px; line-height: 24px; }
  .person__role { color: var(--muted); font-size: 13px; }
  .services {
    position: absolute;
    top: 160px; left: 24px;
    width: 272px;
    list-style: none;
    text-align: right;
    font-size: 16px;
    line-height: 22px;
    white-space: nowrap;
  }
  .contact {
    position: absolute;
    top: 178px; left: 318px;
    list-style: none;
    font-size: 14px;
    line-height: 26px;
    white-space: nowrap;
  }
  .contact li { display: flex; align-items: center; gap: 10px; }
  .contact svg { width: 15px; height: 15px; flex: none; }
</style>
</head>
<body>

  <section class="card card--front" aria-label="Business card front">
    <div class="website">
      <svg viewBox="0 0 16 16" fill="none" stroke="#f2f2f2" stroke-width="1.3" aria-hidden="true">
        <circle cx="8" cy="8" r="7"/><ellipse cx="8" cy="8" rx="3" ry="7"/><line x1="1" y1="8" x2="15" y2="8"/>
      </svg>
      <span>www.ktwelec.example.com.au</span>
    </div>
    <div class="brand">
      <span class="brand__dot"></span>
      <span class="brand__name">KTW ELECTRICAL AND DATA</span>
    </div>
    <div class="tagline">
      <span class="tagline__bar tagline__bar--left"></span>
      <span class="tagline__text">24 HOUR EMERGENCY BREAKDOWN REPAIR</span>
      <span class="tagline__bar tagline__bar--right"></span>
    </div>
  </section>

  <section class="card card--back" aria-label="Business card back">
    <div class="person">
      <p class="person__name">Martin Pellowe</p>
      <p class="person__role">Chief Exective</p>
    </div>
    <div class="brand">
      <span class="brand__dot"></span>
      <span class="brand__name">KTW ELECTRICAL AND DATA</span>
    </div>
    <ul class="services">
      <li>Electrical</li>
      <li>Cctv, security</li>
      <li>Air-conditioning</li>
      <li>Data, communication</li>
      <li>Domestic, commercial, industrial</li>
    </ul>
    <ul class="contact">
      <li>
        <svg viewBox="0 0 16 16" fill="#f2f2f2" aria-hidden="true">
          <path d="M4 1.5l2.2 3-1.3 1.4c.7 1.8 2 3.2 3.9 4l1.3-1.3 3 2.1-1.2 2.5C7 13.5 2.5 9 1.8 3z"/>
        </svg>
        <span>0418 362 927</span>
      </li>
      <li>
        <svg viewBox="0 0 16 16" fill="none" stroke="#f2f2f2" stroke-width="1.4" aria-hidden="true">
          <rect x="1" y="3" width="14" height="10"/><polyline points="1,3 8,9 15,3"/>
        </svg>
        <span>info@ktwelec.example.com.au</span>
      </li>
    </ul>
  </section>

</body>
</html>
```